2-sided Postcard Design

We are an artisan chocolate candy company. We are inspired by old world Spanish candies and love to experiment with new and exciting flavor combinations. You can view our current Chatterly/Quippit page for logo and photos @PicoRamaVT. The brochure is for prospective vendors (i.e. grocery/retail stores) who will be carrying our boxed candies.
Updates

Project Deadline Extended
Reason: I'm posting the pics in about an hour- Thanks for your help!

Check the discussions as I have added the things you guys asked for-

Thanks!

Hey there! As you will note the due date has changed (there was a glitch in the system previously). Just for clarification the deadline is indeed Thursday, May 3rd. Looking forward to seeing what you've got!

Thanks!

Target Market(s)

well-traveled adults who enjoy candy, etc.

Industry/Entity Type

It Company

Requirements
Must have
• 2-sided: side #1-logo with company info summary, side #2-menu of items, company offerings, etc.

I attached info regarding the flavors we have featured already. It's just a starting point. It doesn't necessarily need to have all of them listed as add and remove items weekly from the menu. I'd also like to show that we have gluten-free and nut-free options as well as we will be adding sugar free and dairy free candies in the future.

Please also include the following information as well: we use local ingredients where available, we offer new flavors weekly, we make artisan, small batch, hand-dipped candies, we offer personalized flavors as well. Feel free to change wording, etc. as I am not the best when it comes to diction.

I am getting them printed from brelvo.example. Here are their artwork guidelines: http://us.brelvo.example/help/faq/design-overview.html

Also, please include Chatterly and quippit logo and @PicoRamaVT
Nice to have
• 1-2 pictures of product on side #2 (I will upload the pictures 5/2/12), simplistic in design

Should not have
• too much info, graphics, etc.

```html
<!DOCTYPE html>
<html lang="en">
<head>
<meta charset="utf-8">
<title>Pico Rama – Two-Sided Postcard</title>
<link rel="stylesheet" href="https://fonts.googleapis.com/css2?family=Josefin+Sans:wght@300;400;700&display=swap">
<style>
  :root {
    --paper: #9d6c2a;
    --frame-yellow: #fde300;
    --frame-pink: #ec1a8c;
    --ink-white: #ffffff;
    --ink-yellow: #fde300;
    --label-pink: #ec1a8c;
    --page: #ffffff;
    --art-warm: #c98a3a;
    --art-deep: #6e4a1c;
  }
  * { box-sizing: border-box; margin: 0; padding: 0; }
  html, body {
    width: 1200px; height: 900px; overflow: hidden;
    background: var(--page);
    font-family: "Josefin Sans", "Century Gothic", sans-serif;
  }
  .canvas { position: relative; width: 1200px; height: 900px; }

  .postcard {
    position: absolute; top: 22px;
    width: 564px; height: 784px;
    box-shadow: 4px 5px 6px rgba(0,0,0,0.45);
  }
  .postcard--front { left: 24px; }
  .postcard--back  { left: 614px; }

  .postcard__frame { position: absolute; inset: 0; width: 564px; height: 784px; display: block; }
  .postcard__content { position: absolute; inset: 0; color: var(--ink-white); text-align: center; }

  /* Front */
  .mascot-art {
    position: absolute; left: 182px; top: 80px; width: 206px; height: 300px;
    background: linear-gradient(to bottom, var(--art-warm), var(--art-deep));
    border-radius: 6px;
  }
  .brand-name {
    position: absolute; left: 0; right: 0; top: 402px;
    font-weight: 700; font-size: 66px; line-height: 80px; letter-spacing: 4px;
    color: var(--frame-pink); text-transform: uppercase;
  }
  .tagline {
    position: absolute; left: 0; right: 0; top: 546px;
    font-weight: 300; font-size: 35px; line-height: 40px;
  }

  /* Back */
  .offerings-title {
    position: absolute; left: 0; right: 0; top: 70px;
    font-weight: 700; font-size: 27px; line-height: 33px; letter-spacing: 3px;
    color: var(--ink-yellow); text-transform: uppercase;
  }
  .menu { position: absolute; left: 0; right: 0; top: 142px; list-style: none; }
  .menu__item { font-weight: 300; font-size: 31px; line-height: 53px; }
  .promises {
    position: absolute; left: 0; right: 0; top: 470px;
    font-weight: 700; font-size: 27px; line-height: 47px; letter-spacing: 2px;
    color: var(--ink-yellow); text-transform: uppercase;
  }
  .dietary {
    position: absolute; left: 0; right: 0; top: 574px;
    font-weight: 300; font-size: 20px; line-height: 33px; letter-spacing: 0.6px;
  }
  .social {
    position: absolute; left: 0; right: 0; top: 666px;
    display: flex; justify-content: center; align-items: center; gap: 16px;
    font-size: 25px;
  }
  .social__network { display: flex; align-items: center; gap: 8px; color: var(--ink-yellow); font-weight: 400; }
  .social__dot { width: 22px; height: 22px; border-radius: 50%; background: var(--ink-yellow); }
  .social__handle { font-weight: 300; font-size: 31px; color: var(--ink-white); }

  .side-label {
    position: absolute; top: 830px;
    font-weight: 300; font-size: 44px; color: var(--label-pink);
  }
  .side-label--front { right: 618px; }
  .side-label--back  { right: 24px; }
</style>
</head>
<body>
<main class="canvas">
  <svg width="0" height="0" style="position:absolute">
    <defs>
      <g id="card-frame">
        <rect width="564" height="784" fill="var(--frame-yellow)"/>
        <rect x="16" y="16" width="532" height="752" fill="var(--frame-pink)"/>
        <rect x="26" y="26" width="512" height="732" fill="var(--paper)"/>
        <g fill="var(--frame-pink)">
          <circle cx="0" cy="0" r="68"/><circle cx="564" cy="0" r="68"/>
          <circle cx="0" cy="784" r="68"/><circle cx="564" cy="784" r="68"/>
        </g>
        <g fill="var(--frame-yellow)">
          <circle cx="0" cy="0" r="58"/><circle cx="564" cy="0" r="58"/>
          <circle cx="0" cy="784" r="58"/><circle cx="564" cy="784" r="58"/>
        </g>
        <g fill="var(--paper)">
          <circle cx="0" cy="0" r="44"/><circle cx="564" cy="0" r="44"/>
          <circle cx="0" cy="784" r="44"/><circle cx="564" cy="784" r="44"/>
        </g>
      </g>
    </defs>
  </svg>

  <section class="postcard postcard--front">
    <svg class="postcard__frame" viewBox="0 0 564 784" aria-hidden="true"><use href="#card-frame"/></svg>
    <div class="postcard__content">
      <div class="mascot-art" role="img" aria-label="Brand mascot illustration"></div>
      <h1 class="brand-name">Pico Rama</h1>
      <p class="tagline">Small-batch, traditional<br>Spanish chocolates and<br>confections inspired by<br>Old World recipes</p>
    </div>
  </section>

  <section class="postcard postcard--back">
    <svg class="postcard__frame" viewBox="0 0 564 784" aria-hidden="true"><use href="#card-frame"/></svg>
    <div class="postcard__content">
      <h2 class="offerings-title">Just a few of our<br>delectable offerings...</h2>
      <ul class="menu">
        <li class="menu__item">Spicy Key Lime CocoLimas</li>
        <li class="menu__item">Mexican Hot Chocolate Truffles</li>
        <li class="menu__item">Tres Lunas Ancho Chile Truffles</li>
        <li class="menu__item">Spicy Peanut Butter Bites</li>
        <li class="menu__item">Citrus Lavender Truffles</li>
        <li class="menu__item">Mazapanes</li>
      </ul>
      <p class="promises">Local ingredients.<br>New flavors weekly.</p>
      <p class="dietary">Gluten-free and nut-free candies available.<br>Sugar-free and dairy-free candies coming soon!</p>
      <div class="social">
        <span class="social__network"><span class="social__dot"></span>Chatterly</span>
        <span class="social__handle">@PicoRamaVT</span>
        <span class="social__network">Quippit<span class="social__dot"></span></span>
      </div>
    </div>
  </section>

  <p class="side-label side-label--front">Side 1</p>
  <p class="side-label side-label--back">Side 2</p>
</main>
</body>
</html>
```